Tarnby Website

We need a web design for our company based in Sydney. Our company does many and varied acitivities. From private investments, licencing, business consultacy, payment solutions.

Our services focus on our client’s critical opportunities. We provide a range of services including strategy, marketing, compliance, organization and technology.

We can unlock your growth and potential and deliver on core strategy. We add value and bring extensive expertise in optimizing your results.

We provide also provide the following services:

 private investments,
 licensing,
 business consultancy,
 payment solutions.

Target Market(s)

Businesses

Coding

Coded - Design and coding required

Number of Pages Required

3 page

Colors

Designer to choose colors to be used in the design.

Requirements
Must have
• Corporate look and feel. two touch points, email info@tarnby.com.au and a phone number TBA
• MUST include logos and branding from attached
Nice to have
• photos

```html
<!DOCTYPE html>
<html lang="en">
<head>
<meta charset="utf-8">
<title>Tarnby</title>
<link href="https://fonts.googleapis.com/css2?family=Poppins:ital,wght@0,400;0,500;0,600;0,700;1,400&display=swap" rel="stylesheet">
<style>
:root{
  --ink:#222;
  --muted:#777;
  --blue:#2f74b5;
  --blue-bright:#3b8fd6;
  --band:#f0f0f0;
  --black:#0b0b0b;
  --white:#fff;
  --line:#dcdcdc;
}
*{margin:0;padding:0;box-sizing:border-box}
html,body{width:1200px;height:3169px;overflow:hidden}
body{font-family:"Poppins",sans-serif;color:var(--ink);background:var(--white);position:relative}
.abs{position:absolute}

/* header */
.site-header{position:absolute;left:0;top:0;width:1200px;height:78px;background:var(--black);color:var(--white)}
.brand{position:absolute;left:160px;top:20px;font-weight:700;font-size:32px;color:var(--white);line-height:38px;display:flex;align-items:center;gap:10px}
.brand .dot{width:14px;height:14px;border-radius:50%;background:var(--blue-bright)}
.main-nav{position:absolute;left:0;top:0;width:760px;height:78px;font-size:12px;font-weight:500}
.main-nav a{position:absolute;top:31px;line-height:16px;color:var(--white);text-decoration:none;white-space:nowrap}
.main-nav a.active{color:var(--blue-bright)}
.header-divider{position:absolute;left:750px;top:18px;width:1px;height:42px;background:#444}
.quick-label{position:absolute;left:790px;top:19px;font-size:12px;line-height:20px;color:var(--blue-bright);font-weight:500}
.header-contact{position:absolute;left:866px;top:19px;font-size:12px;line-height:20px}
.header-contact div{display:flex;align-items:center;gap:10px;white-space:nowrap}

/* hero */
.hero{position:absolute;left:0;top:78px;width:1200px;height:577px;background:linear-gradient(180deg,#0d3aa6 0%,#1a4fc4 30%,#2a3f7a 55%,#1d2440 72%,#0f2a55 100%)}
.hero-title{position:absolute;left:0;top:140px;width:1200px;text-align:center;font-weight:700;font-size:110px;color:var(--white);line-height:120px}

/* sections */
.section-title{position:absolute;left:0;width:1200px;text-align:center;font-weight:600;font-size:22px;color:#333;letter-spacing:.5px;line-height:30px}
.section-lead{position:absolute;left:0;width:1200px;text-align:center;font-size:11px;line-height:20px;color:#444;white-space:nowrap}

.services{position:absolute;left:0;top:655px;width:1200px;height:423px;background:var(--band)}
.service-card{position:absolute;top:102px;width:202px;height:230px;background:var(--white);border:1px solid var(--line);text-align:center}
.service-card svg{margin-top:30px}
.service-card h3{font-size:14px;font-weight:500;margin-top:14px;color:#222}
.service-card p{font-size:11px;line-height:17px;color:var(--muted);margin:8px 24px 0}

.other{position:absolute;left:0;top:1078px;width:1200px;height:729px;background:linear-gradient(180deg,#fff 0%,#fff 45%,#dbe8f4 80%,#c9dcee 100%)}

.testimonials{position:absolute;left:0;top:1807px;width:1200px;height:406px;background:linear-gradient(180deg,#1c1c1e,#2a2a2c 60%,#202022)}
.testimonials .section-title{color:var(--white);top:80px}
.quote{position:absolute;left:290px;top:130px;width:620px;text-align:center;color:#e8e8e8;font-style:italic;font-size:17.5px;line-height:35px}
.quote-author{position:absolute;left:0;top:252px;width:1200px;text-align:center;color:var(--white);font-size:13px;font-weight:600}
.dots{position:absolute;left:578px;top:330px;display:flex;gap:6px}
.dots span{width:10px;height:10px;border-radius:50%;background:var(--white)}
.dots span.off{background:transparent;border:1px solid #ccc}

.news{position:absolute;left:0;top:2213px;width:1200px;height:559px;background:var(--white)}
.news-card{position:absolute;top:158px;width:282px;height:344px;border:1px solid var(--line);background:var(--white)}
.news-image{height:169px;width:100%}
.news-meta{display:flex;gap:16px;font-size:11px;color:var(--blue);margin:22px 16px 0}
.news-card h3{font-size:14.5px;font-weight:400;line-height:23px;margin:18px 16px 0;color:#222}
.read-more{font-size:11px;color:var(--muted);margin:14px 24px 0}

.contact-band{position:absolute;left:0;top:2772px;width:1200px;height:81px;background:linear-gradient(90deg,#3a86c8,#2c6fb0);color:var(--white);font-size:22px;font-weight:500}
.contact-band span{position:absolute;top:24px;white-space:nowrap;display:flex;align-items:center;gap:12px}

.site-footer{position:absolute;left:0;top:2853px;width:1200px;height:316px;background:linear-gradient(180deg,#fff,#ededed)}
.footer-brand{position:absolute;left:160px;top:60px;font-weight:700;font-size:44px;color:var(--blue);line-height:50px}
.socials{position:absolute;left:162px;top:142px;display:flex;gap:16px;align-items:center}
.socials .circle{width:20px;height:20px;border-radius:50%;background:#8a8a8a}
.footer-col{position:absolute;top:50px;font-size:11.5px;line-height:25.5px;color:#333;white-space:nowrap}
.footer-col h4{font-size:15px;font-weight:500;margin-bottom:10px}
.copyright{position:absolute;left:0;top:272px;width:1200px;text-align:center;font-size:11px;color:#333}
</style>
</head>
<body>

<header class="site-header">
  <div class="brand"><span class="dot"></span>Tarnby</div>
  <nav class="main-nav">
    <a class="active" style="left:338px">HOME</a>
    <a style="left:401px">ABOUT US</a>
    <a style="left:494px">SERVICES</a>
    <a style="left:579px">NEWS</a>
    <a style="left:642px">CONTACT</a>
  </nav>
  <div class="header-divider"></div>
  <div class="quick-label">QUICK<br>CONTACT</div>
  <div class="header-contact">
    <div><svg width="10" height="8" viewBox="0 0 10 8"><rect width="10" height="8" fill="#fff"/><path d="M0 0 L5 4 L10 0" stroke="#0b0b0b" fill="none"/></svg>Email info@tarnby.com.au</div>
    <div><svg width="10" height="10" viewBox="0 0 10 10"><path d="M2 0 L4 0 L4.5 3 L3 4 Q4.5 6.5 6 7 L7 5.5 L10 6 L10 8 Q10 10 8 10 Q0 9 0 2 Q0 0 2 0Z" fill="#fff"/></svg>Phone number 1- 800 - 555 018</div>
  </div>
</header>

<section class="hero" role="img" aria-label="Night photograph of a harbour city skyline with a bridge and waterfront landmark, lights reflected on the water">
  <div class="hero-title">Tarnby</div>
</section>
<svg viewBox="0 0 1200 100" preserveAspectRatio="none" style="position:absolute;left:0;top:570px;width:1200px;height:100px">
  <path d="M0 80 Q600 -30 1200 80 L1200 100 L0 100Z" fill="#f0f0f0"/>
</svg>

<section class="services">
  <h2 class="section-title" style="top:-26px">SERVICES</h2>
  <p class="section-lead" style="top:17px">Sed ut perspiciatis unde omnis iste natus error sit voluptatem accusantium doloremque lauda<br>ntium, totam rem aperiam, eaque ipsa quae ab illo inventore veritatis et quasi architec.</p>

  <div class="service-card" style="left:160px">
    <svg width="72" height="64" viewBox="0 0 72 64" fill="none" stroke="#2f74b5" stroke-width="2.5"><path d="M20 14 L26 4 L34 14 Z"/><path d="M18 16 Q4 34 10 52 Q24 60 38 52 Q44 34 36 16 Z" fill="#dbe9f6"/><text x="22" y="44" font-size="18" fill="#2f74b5" stroke="none" font-family="Poppins,sans-serif" font-weight="700">$</text><ellipse cx="56" cy="32" rx="12" ry="4"/><ellipse cx="56" cy="40" rx="12" ry="4"/><ellipse cx="56" cy="48" rx="12" ry="4"/><ellipse cx="56" cy="56" rx="12" ry="4"/></svg>
    <h3>Private Investments</h3>
    <p>Sed ut perspiciatis undmnis iste natus siciati rorsit.</p>
  </div>
  <div class="service-card" style="left:387px">
    <svg width="72" height="64" viewBox="0 0 72 64" fill="none" stroke="#2f74b5" stroke-width="2.5"><rect x="14" y="4" width="36" height="48" fill="#dbe9f6"/><path d="M20 14 H44 M20 22 H44 M20 30 H36"/><rect x="50" y="10" width="8" height="20"/><circle cx="32" cy="44" r="7" fill="#fff"/><path d="M28 50 L26 60 L32 56 L38 60 L36 50"/></svg>
    <h3>Licensing</h3>
    <p>Sed ut perspiciatis undmnis iste natus siciati rorsit.</p>
  </div>
  <div class="service-card" style="left:614px">
    <svg width="72" height="64" viewBox="0 0 72 64" fill="none" stroke="#2f74b5" stroke-width="2.5"><rect x="8" y="4" width="22" height="14" fill="#dbe9f6"/><rect x="40" y="4" width="22" height="14"/><circle cx="20" cy="32" r="6"/><circle cx="52" cy="32" r="6"/><path d="M8 58 Q8 42 20 42 Q32 42 32 58Z" fill="#dbe9f6"/><path d="M40 58 Q40 42 52 42 Q64 42 64 58Z" fill="#dbe9f6"/></svg>
    <h3>Business Consultancy</h3>
    <p>Sed ut perspiciatis undmnis iste natus siciati rorsit.</p>
  </div>
  <div class="service-card" style="left:841px">
    <svg width="80" height="64" viewBox="0 0 80 64" fill="none" stroke="#2f74b5" stroke-width="2.5"><rect x="14" y="6" width="58" height="36" rx="3"/><rect x="6" y="16" width="60" height="38" rx="3" fill="#dbe9f6"/><path d="M6 26 H66"/><circle cx="48" cy="44" r="5"/><circle cx="56" cy="44" r="5"/></svg>
    <h3>Payment Solutions</h3>
    <p>Sed ut perspiciatis undmnis iste natus siciati rorsit.</p>
  </div>
</section>

<section class="other">
  <h2 class="section-title" style="top:62px">OTHER SERVICES</h2>
  <p class="section-lead" style="top:103px">Sed ut perspiciatis unde omnis iste natus error sit voluptatem accusantium doloremque lauda<br>ntium, totam rem aperiam, eaque ipsa quae ab illo inventore veritatis et quasi architec.</p>
  <svg class="abs" style="left:0;top:0" width="1200" height="729" viewBox="0 0 1200 729" font-family="Poppins,sans-serif">
    <defs>
      <linearGradient id="photoDark" x1="0" y1="0" x2="1" y2="1"><stop offset="0" stop-color="#3a3f4a"/><stop offset="1" stop-color="#15171c"/></linearGradient>
      <linearGradient id="photoTech" x1="0" y1="0" x2="1" y2="1"><stop offset="0" stop-color="#1e2a4a"/><stop offset="1" stop-color="#0e1526"/></linearGradient>
    </defs>
    <g role="img" aria-label="Photo of an office desk with laptop and papers">
      <polygon points="600,168 748,316 600,464 452,316" fill="url(#photoDark)" stroke="#fff" stroke-width="3"/>
    </g>
    <g role="img" aria-label="Photo of a hand touching a digital interface">
      <polygon points="894,168 1042,316 894,464 746,316" fill="url(#photoDark)" stroke="#fff" stroke-width="3"/>
    </g>
    <polygon points="306,168 454,316 306,464 158,316" fill="#0c0f16" stroke="#fff" stroke-width="3"/>
    <polygon points="306,186 436,316 306,446 176,316" fill="#2f5f9a"/>
    <g role="img" aria-label="Photo of a network of connected people icons">
      <polygon points="452,327 600,475 452,623 304,475" fill="url(#photoTech)" stroke="#fff" stroke-width="3"/>
    </g>
    <g role="img" aria-label="Photo of glowing technology circuits">
      <polygon points="746,327 894,475 746,623 598,475" fill="url(#photoTech)" stroke="#fff" stroke-width="3"/>
    </g>
    <g fill="#fff" font-size="17" text-anchor="middle">
      <text x="306" y="322">Strategy</text>
      <text x="600" y="322">Marketing</text>
      <text x="894" y="322">Compliance</text>
      <text x="452" y="481">Organisation</text>
      <text x="746" y="481">Technology</text>
    </g>
  </svg>
</section>

<section class="testimonials" role="img" aria-label="Dark faded photograph of a harbour bridge behind the testimonial">
  <h2 class="section-title">TESTIMONIALS</h2>
  <p class="quote">" Sed ut perspiciatis unde omnis iste natus error siuataccusan tiumdremque laudantiumtd ut erspiciatis unde omnis iste natus error siuatem accusa ntiuiciatis unde om mdrem "</p>
  <p class="quote-author">Mara Ellison, City Name</p>
  <div class="dots"><span class="off"></span><span></span><span></span></div>
</section>

<section class="news">
  <h2 class="section-title" style="top:54px">LATEST NEWS</h2>
  <p class="section-lead" style="top:95px">Sed ut perspiciatis unde omnis iste natus error sit voluptatem accusantium doloremque lauda<br>ntium, totam rem aperiam, eaque ipsa quae ab illo inventore veritatis et quasi architec.</p>

  <article class="news-card" style="left:160px">
    <div class="news-image" role="img" aria-label="Photo of hands typing on a laptop beneath a megaphone sketch" style="background:linear-gradient(180deg,#555,#2a2a2a)"></div>
    <div class="news-meta"><span>▢ Apr 18,2018</span><span>● Admin</span></div>
    <h3>Sed ut perspiciatis unde omnisa tus error sit voluptatem accusanu mdoloremque laudantium.</h3>
    <p class="read-more">Read More</p>
  </article>
  <article class="news-card" style="left:459px">
    <div class="news-image" role="img" aria-label="Photo of a business person working with charts on a desk" style="background:linear-gradient(135deg,#6a7a8c,#c58a4a 60%,#3a4a5c)"></div>
    <div class="news-meta"><span>▢ Apr 18,2018</span><span>● Admin</span></div>
    <h3>Sed ut perspiciatis unde omnisa tus error sit voluptatem accusanu mdoloremque laudantium.</h3>
    <p class="read-more">Read More</p>
  </article>
  <article class="news-card" style="left:757px">
    <div class="news-image" role="img" aria-label="Photo of a person holding a card while using a laptop" style="background:linear-gradient(135deg,#e8eef3,#9aa8b6 60%,#3c4a63)"></div>
    <div class="news-meta"><span>▢ Apr 18,2018</span><span>● Admin</span></div>
    <h3>Sed ut perspiciatis unde omnisa tus error sit voluptatem accusanu mdoloremque laudantium.</h3>
    <p class="read-more">Read More</p>
  </article>
</section>

<section class="contact-band">
  <span style="left:176px">Quick contact</span>
  <span style="left:382px"><svg width="24" height="18" viewBox="0 0 24 18"><rect width="24" height="18" rx="2" fill="#fff"/><path d="M1 1 L12 10 L23 1" stroke="#2f74b5" stroke-width="2" fill="none"/></svg>Email info@tarnby.com.au</span>
  <span style="left:746px"><svg width="26" height="26" viewBox="0 0 26 26" fill="none" stroke="#fff" stroke-width="2"><path d="M5 2 L9 2 L10 8 L7 10 Q10 16 16 19 L18 16 L24 17 L24 21 Q24 25 20 25 Q2 23 1 6 Q1 2 5 2Z"/></svg>Phone: 1- 800 - 555 018</span>
</section>

<footer class="site-footer">
  <div class="footer-brand">Tarnby</div>
  <div class="socials">
    <svg width="24" height="18" viewBox="0 0 24 18"><rect width="24" height="18" rx="2" fill="#8a8a8a"/><path d="M1 1 L12 10 L23 1" stroke="#fff" stroke-width="2" fill="none"/></svg>
    <span class="circle"></span><span class="circle"></span><span class="circle"></span>
  </div>
  <div class="footer-col" style="left:421px"><h4>Links</h4>Home<br>About<br>Services<br>What We do<br>News</div>
  <div class="footer-col" style="left:557px"><h4>Projects</h4>Sed uerspiciatiem<br>Comnisteatusit<br>Sed uerspiciatiem<br>Comnisteatusit<br>Perspiciatis unde</div>
  <div class="footer-col" style="left:741px"><h4>Policies</h4>Privacy<br>Complaint and Feedback<br>Comnisteatusit<br>Perspiciatis unde</div>
  <div class="footer-col" style="left:936px"><h4>Other Links</h4>Sed uterspiciatis<br>Sed uerspiciatiem<br>Comnisteatusit<br>Perspiciatis unde<br>Sed uerspiciatiem</div>
  <p class="copyright">© 2018 Tarnby. All Rights are Reserved.&nbsp; Privacy Policy | Terms of Use | Contact</p>
</footer>

</body>
</html>
```